Presentation of Business Project of Implementing CRM for a car Detailing Company

We need a professional PowerPoint presentation template (5 slides) for a business presentation about implementing a CRM system at Ravenmoor Detailing, a premium automotive detailing company in South Africa.
About the Company:
Ravenmoor Detailing specializes in high-end car detailing, paint protection, leather repair, and classic car restoration. They're a premium service provider looking to modernize their customer management through digital transformation.
What We Need:
A visually impressive presentation template with 5 key slide designs that we can duplicate and reuse across our full presentation. The presentation will show how a ChatterLoop-integrated CRM system can help the business grow from 60% to 80% customer retention, free up the owner's time, and enable expansion.
The 5 Slides:

Title slide - Space for project title + 5 team member names (impactful opening)
Content slide - Standard layout with bullet points (we'll duplicate this for 10+ slides)
Large data table - For vendor comparisons (4 rows × 10 columns)
Financial charts - 3 side-by-side scenario comparisons with bar/column charts
Simple table - For cost breakdowns (2-3 columns)

Design Style:
Modern, polished, and eye-catching. Should look professional but capture attention - think sleek automotive industry meets premium business consulting. Bold use of car detailing/workshop imagery as backgrounds where appropriate. Contemporary color scheme. Clean layouts that make data easy to read but NOT boring.

Images:
We will provide a link to high-quality car detailing and workshop images that you can integrate into the design (backgrounds, accents, visual interest).

https://www.filebarrow-share.example/drive/7kqLm2TzvPeXn9RwY4HsJ-bGD#RavenmoorDetailing

Link contain image of company actual work and logo of the company. The idea is to use their images.

Important:
All tables and charts should be editable so we can add our own data. Slides should be easy to duplicate and modify.

Deliverables:
5 PowerPoint slides (.pptx) - fully editable
Google Slides version
Fonts/colors consistent throughout

```html
<!DOCTYPE html>
<html lang="en">
<head>
<meta charset="utf-8">
<title>Ravenmoor Detailing – Vision to Reality slide system</title>
<link href="https://fonts.googleapis.com/css2?family=Arimo:wght@400;700&display=swap" rel="stylesheet">
<style>
:root{
  --bg:#d9d6d7;
  --red:#e4222a;
  --ink:#1b1b1b;
  --carbon:#2a2a2c;
  --carbon-dark:#171718;
  --paper:#ffffff;
  --paper-shade:#e6e6e6;
  --rule:#e4222a;
  --muted:#555;
  --row-a:#f3f3f3;
  --row-b:#e2e2e2;
}
*{box-sizing:border-box;margin:0;padding:0}
html,body{width:1186px;height:1200px;overflow:hidden;background:var(--bg);font-family:"Arimo",Arial,sans-serif;color:var(--ink)}
.canvas{position:relative;width:1186px;height:1200px}
.slide{position:absolute;width:327px;height:184px;overflow:hidden;background:linear-gradient(180deg,var(--paper) 40%,var(--paper-shade))}
.col-1{left:63px}.col-2{left:427px}.col-3{left:790px}
.row-1{top:53px}.row-2{top:253px}.row-3{top:453px}.row-4{top:653px}.row-alt{top:955px}
.section-label{position:absolute;top:907px;font-size:25px;font-weight:400;color:#111}
.photo{position:absolute}
.band{position:absolute;left:0;top:0;height:41px;background:linear-gradient(180deg,#3a3a3c,var(--carbon-dark))}
.slide-title{position:absolute;left:25px;top:12px;font-size:17px;color:#f2f2f2;white-space:nowrap}
.slide-title.dark{color:var(--ink)}
.accent{color:var(--red)}
.badge{position:absolute;width:27px;height:22px;background:#111;border:1px solid #444;display:flex;align-items:center;justify-content:center;text-align:center;font-size:3px;line-height:1.2;color:#ddd}
.footer-brand{position:absolute;left:23px;bottom:12px;font-size:4px;font-weight:700;color:#111}
.footer-rule{position:absolute;left:23px;right:20px;bottom:9px;height:0.5px;background:var(--rule)}
.page-no{position:absolute;right:20px;bottom:11px;font-size:5px;color:#333}
.body-copy{position:absolute;font-size:4.2px;line-height:1.75;color:#222}
.toc{position:absolute;left:24px;top:62px;list-style:none}
.toc li{display:flex;align-items:center;height:16.7px;font-size:5.2px}
.num{display:inline-block;width:14px;height:7px;background:var(--red);color:#fff;font-size:4.5px;text-align:center;line-height:7px;margin-right:7px;transform:skewX(-15deg)}
table.data{position:absolute;border-collapse:collapse;font-size:4px}
table.data th{background:var(--red);color:#fff;font-weight:700;height:11px;padding:0 2px}
table.data td{height:11.3px;text-align:center;padding:0 2px}
table.data td.lbl{text-align:left;font-weight:700}
table.data tr:nth-child(odd) td{background:var(--row-a)}
table.data tr:nth-child(even) td{background:var(--row-b)}
.goal-item{position:absolute;font-size:3px;line-height:1.4;color:#333}
.goal-item b{display:block;color:var(--red);font-size:3.2px;margin-bottom:1px}
.dark-slide{background:linear-gradient(135deg,#303032,var(--carbon-dark))}
.names{position:absolute;left:0;right:0;bottom:10px;display:flex;justify-content:space-around;font-size:5.5px;font-weight:700;color:#f1f1f1}
.brand-name{color:#f2f2f2;font-weight:400;text-align:center}
.contact-lines{position:absolute;left:25px;top:104px;font-size:5px;color:var(--red)}
.contact-lines div{height:17px}
.dots{position:absolute;left:25px;top:152px;display:flex;gap:3px}
.dots span{width:7px;height:7px;border-radius:50%;background:var(--red)}
</style>
</head>
<body>
<div class="canvas">

<!-- 1 Cover -->
<section class="slide dark-slide col-1 row-1">
  <div class="photo" role="img" aria-label="Black sports coupe bursting through glowing orange particles" style="inset:0;background:radial-gradient(ellipse at 50% 60%,#6b4a22 0%,#2b1e12 45%,#0d0d0d 90%)"></div>
  <div class="badge" style="left:19px;top:8px;width:54px;height:43px;font-size:5px">Ravenmoor Detailing</div>
  <div class="slide-title" style="left:83px;top:18px;font-size:27px;font-weight:700">Vision <span style="font-weight:400">to</span> <span class="accent">Reality</span></div>
  <div class="names"><span>Insert Name</span><span>Insert Name</span><span>Insert Name</span><span>Insert Name</span><span>Insert Name</span></div>
</section>

<!-- 2 Contents -->
<section class="slide col-2 row-1">
  <div class="photo" role="img" aria-label="Detailer applying protection film to a white car headlight" style="inset:0;clip-path:polygon(164px 0,327px 0,327px 184px,131px 184px);background:linear-gradient(135deg,#b9bcc0,#4c4f55 60%,#1e1f22)"></div>
  <div class="band" style="width:327px;clip-path:polygon(0 0,327px 0,327px 41px,0 41px)"></div>
  <div class="slide-title" style="color:var(--red)">Contents</div>
  <div class="badge" style="left:282px;top:14px">Ravenmoor<br>Detailing</div>
  <ul class="toc">
    <li><span class="num">03</span>Goals &amp; Objectives</li>
    <li><span class="num">04</span>Vendor Comparison</li>
    <li><span class="num">05</span>Scenario Comparison</li>
    <li><span class="num">06</span>Cost Breakdown</li>
    <li><span class="num">07</span>Contact Us</li>
  </ul>
  <div class="footer-rule" style="right:140px"></div>
  <div class="page-no" style="left:23px;right:auto">02</div>
  <div class="footer-brand" style="left:41px">Vision to <span class="accent">Reality</span></div>
</section>

<!-- 3 Goals -->
<section class="slide col-3 row-1">
  <div class="photo" role="img" aria-label="Car interior with black and red sports seats" style="inset:0;clip-path:polygon(0 0,262px 0,189px 184px,0 184px);background:linear-gradient(135deg,#4a4a4e,#1a1a1c 60%,#5a1a1c)"></div>
  <div class="band" style="width:262px;clip-path:polygon(0 0,262px 0,236px 41px,0 41px)"></div>
  <div class="slide-title">Goals &amp; <span class="accent">Objectives</span></div>
  <div class="badge" style="left:281px;top:15px">Ravenmoor<br>Detailing</div>
  <div class="body-copy" style="left:24px;top:59px;width:100px;height:83px;padding:6px;background:rgba(255,255,255,.14);border-radius:4px;color:#eee;font-size:3.6px">Lorem ipsum dolor sit amet, consectetuer adipiscing elit, sed diam nonummy nibh zzril delenit augue duis dolore te feugait nulla facilisi. Lorem ipsum dolor sit amet, cons ectetuer ullamcorper suscipit lobortis nisl ut aliquip ex ea commodo consequat.</div>
  <svg style="position:absolute;left:193px;top:61px" width="10" height="85" viewBox="0 0 10 85" fill="none" stroke="#e4222a" stroke-width=".8"><path d="M1 9h8M2 8V5M4 8V3M6 8V4M8 8V1"/><rect x="2" y="24" width="5" height="6"/><path d="M1 47a4 4 0 0 1 7-2M9 49a4 4 0 0 1-7 2"/><circle cx="5" cy="72" r="4" stroke-dasharray="2 1"/></svg>
  <div class="goal-item" style="left:214px;top:60px;width:95px"><b>Revenue Growth</b>Lorem ipsum dolor sit amet, consectetur adipiscing elit sed do eiusmod tempor.</div>
  <div class="goal-item" style="left:214px;top:82px;width:95px"><b>Profit Margins</b>Lorem ipsum dolor sit amet, consectetur adipiscing elit sed do eiusmod tempor.</div>
  <div class="goal-item" style="left:214px;top:107px;width:95px"><b>Sustainability</b>Lorem ipsum dolor sit amet, consectetur adipiscing elit sed do eiusmod tempor.</div>
  <div class="goal-item" style="left:214px;top:130px;width:95px"><b>Return On Investment</b>Lorem ipsum dolor sit amet, consectetur adipiscing elit sed do eiusmod tempor.</div>
  <div class="footer-brand" style="color:#eee">Vision to <span class="accent">Reality</span></div>
  <div class="page-no" style="color:#aaa">03</div>
</section>

<!-- 4 Vendor comparison -->
<section class="slide col-1 row-2">
  <div class="photo" role="img" aria-label="Close-up of a silver car front grille and carbon trim" style="inset:0;clip-path:polygon(167px 0,327px 0,327px 184px,167px 184px);background:linear-gradient(135deg,#8a8c90,#2c2d30 70%)"></div>
  <div class="band" style="width:327px"></div>
  <div class="slide-title">Vendor <span class="accent">Comparison</span></div>
  <div class="badge" style="left:280px;top:14px">Ravenmoor<br>Detailing</div>
  <div class="body-copy" style="left:25px;top:59px;width:110px">Lorem ipsum dolor sit amet, consectetur adipiscing elit sed do eiusmod tempor incididunt ut labore et dolore magna aliqua. Ut enim ad minim veniam</div>
  <table class="data" style="left:25px;top:94px;width:282px">
    <tr><th></th><th>Vendor 1</th><th>Vendor 2</th><th>Vendor 3</th><th>Vendor 4</th><th>Vendor 5</th><th>Vendor 6</th><th>Vendor 7</th><th>Vendor 8</th><th>Vendor 9</th><th>Vendor 10</th></tr>
    <tr><td class="lbl">Item 1</td><td>11</td><td>6</td><td>8</td><td>4</td><td>7</td><td>5</td><td>14</td><td>16</td><td>8</td><td>10</td></tr>
    <tr><td class="lbl">Item 2</td><td>15</td><td>12</td><td>15</td><td>8</td><td>12</td><td>11</td><td>15</td><td>10</td><td>15</td><td>7</td></tr>
    <tr><td class="lbl">Item 3</td><td>9</td><td>6</td><td>14</td><td>12</td><td>9</td><td>15</td><td>3</td><td>12</td><td>14</td><td>9</td></tr>
    <tr><td class="lbl">Item 4</td><td>14</td><td>18</td><td>20</td><td>12</td><td>10</td><td>7</td><td>11</td><td>14</td><td>20</td><td>16</td></tr>
  </table>
  <div class="footer-brand">Vision to <span class="accent">Reality</span></div>
  <div class="footer-rule" style="right:160px"></div>
  <div class="page-no" style="color:#ccc">04</div>
</section>

<!-- 5 Scenario comparison -->
<section class="slide col-2 row-2">
  <div class="band" style="width:327px"></div>
  <div class="slide-title">Scenario <span class="accent">Comparison</span></div>
  <div class="badge" style="left:280px;top:14px">Ravenmoor<br>Detailing</div>
  <div class="body-copy" style="left:25px;top:63px;width:100px;font-size:4px;line-height:2.2">Lorem ipsum dolor sit amet, consectetuer adipiscing elit, sed diam nonummy nibh zzril delenit augue duis dolore te feugait nulla facilisi. Lorem ipsum dolor sit amet, cons ectetuer ullamcorper suscipit lobortis nisl ut aliquip ex ea commodo consequat.</div>
  <svg style="position:absolute;left:136px;top:56px" width="150" height="105" viewBox="0 0 150 105" font-family="Arimo, Arial, sans-serif">
    <g font-size="2.5" fill="#333" text-anchor="end">
      <text x="5" y="91">0</text><text x="5" y="76">1</text><text x="5" y="61">2</text><text x="5" y="46">3</text><text x="5" y="31">4</text><text x="5" y="16">5</text><text x="5" y="1.5">6</text>
    </g>
    <line x1="7" y1="90" x2="148" y2="90" stroke="#bbb" stroke-width=".3"/>
    <g><rect x="12" y="25.5" width="5.5" height="64.5" fill="#bdbdbd"/><rect x="19" y="54" width="5.5" height="36" fill="#e4222a"/><rect x="26" y="60" width="5.5" height="30" fill="#111"/></g>
    <g><rect x="47" y="52.5" width="5.5" height="37.5" fill="#bdbdbd"/><rect x="54" y="24" width="5.5" height="66" fill="#e4222a"/><rect x="61" y="60" width="5.5" height="30" fill="#111"/></g>
    <g><rect x="82" y="37.5" width="5.5" height="52.5" fill="#bdbdbd"/><rect x="89" y="63" width="5.5" height="27" fill="#e4222a"/><rect x="96" y="45" width="5.5" height="45" fill="#111"/></g>
    <g><rect x="117" y="22.5" width="5.5" height="67.5" fill="#bdbdbd"/><rect x="124" y="48" width="5.5" height="42" fill="#e4222a"/><rect x="131" y="15" width="5.5" height="75" fill="#111"/></g>
    <g font-size="2.2" fill="#333" text-anchor="middle"><text x="22" y="94">Vendor 1</text><text x="57" y="94">Vendor 2</text><text x="92" y="94">Vendor 3</text><text x="127" y="94">Vendor 4</text></g>
    <g font-size="2.2" fill="#333"><rect x="56" y="96" width="2" height="2" fill="#bdbdbd"/><text x="59" y="98">Item 1</text><rect x="67" y="96" width="2" height="2" fill="#e4222a"/><text x="70" y="98">Item 2</text><rect x="78" y="96" width="2" height="2" fill="#111"/><text x="81" y="98">Item 3</text></g>
  </svg>
  <div class="footer-brand">Vision to <span class="accent">Reality</span></div>
  <div class="footer-rule"></div>
  <div class="page-no">05</div>
</section>

<!-- 6 Cost breakdown -->
<section class="slide col-3 row-2">
  <div class="photo" role="img" aria-label="Steering wheel and red leather seats of a performance saloon" style="inset:0;clip-path:polygon(178px 41px,327px 41px,327px 184px,133px 184px);background:linear-gradient(135deg,#3c3c40,#1b1b1d 55%,#8e1c20)"></div>
  <div class="band" style="width:327px;clip-path:polygon(0 0,327px 0,327px 41px,0 41px)"></div>
  <div class="slide-title" style="top:17px">Cost <span class="accent">Breakdown</span></div>
  <div class="badge" style="left:281px;top:14px">Ravenmoor<br>Detailing</div>
  <div class="body-copy" style="left:25px;top:61px;width:138px">Lorem ipsum dolor sit amet, consectetur adipiscing elit sed do eiusmod tempor incididunt ut labore et dolore magna aliqua. Ut enim ad minim veniam</div>
  <table class="data" style="left:25px;top:98px;width:194px">
    <tr><th></th><th>Vendor 1</th><th>Vendor 2</th><th>Vendor 3</th></tr>
    <tr><td class="lbl">Item 1</td><td>11</td><td>6</td><td>8</td></tr>
    <tr><td class="lbl">Item 2</td><td>15</td><td>12</td><td>15</td></tr>
    <tr><td class="lbl">Item 3</td><td>9</td><td>6</td><td>14</td></tr>
    <tr><td class="lbl">Item 4</td><td>14</td><td>18</td><td>20</td></tr>
  </table>
  <div class="footer-brand">Vision to <span class="accent">Reality</span></div>
  <div class="footer-rule" style="right:200px"></div>
  <div class="page-no" style="color:#bbb">06</div>
</section>

<!-- 7 Portfolio -->
<section class="slide col-1 row-3">
  <div class="band" style="width:200px"></div>
  <div class="badge" style="left:25px;top:15px">Ravenmoor<br>Detailing</div>
  <div class="photo" role="img" aria-label="Red and white coupe in a detailing studio" style="left:170px;top:0;width:157px;height:56px;clip-path:polygon(14px 0,143px 0,157px 30px,143px 56px,26px 56px,0 28px);background:linear-gradient(135deg,#b12126,#3a3b40)"></div>
  <div class="photo" role="img" aria-label="Grey coupe parked in a workshop" style="left:168px;top:59px;width:159px;height:125px;background:linear-gradient(135deg,#5d5f64,#17171a)"></div>
  <div class="photo" role="img" aria-label="Yellow emblem on a wheel hub" style="left:251px;top:56px;width:76px;height:60px;clip-path:polygon(0 30px,15px 0,76px 0,76px 60px,15px 60px);background:linear-gradient(135deg,#2e2f33,#0f0f10)"></div>
  <div style="position:absolute;left:167px;top:56px;width:160px;height:3px;background:#fff"></div>
  <div class="slide-title dark" style="top:46px">Our <span class="accent">Portfolio</span></div>
  <ul class="toc" style="top:70px">
    <li style="height:14.5px"><span class="num">01</span>Corsaro V6 Coupe</li>
    <li style="height:14.5px"><span class="num">02</span>Strale 9 GT Blue-Purple</li>
    <li style="height:14.5px"><span class="num">03</span>Strale GT4 White</li>
    <li style="height:14.5px"><span class="num">04</span>Brennhart M Touring</li>
    <li style="height:14.5px"><span class="num">05</span>Corsaro - Track</li>
    <li style="height:14.5px"><span class="num">06</span>Veloran S3 White</li>
  </ul>
  <div class="footer-rule" style="right:150px"></div>
  <div class="page-no" style="left:23px;right:auto">07</div>
</section>

<!-- 8 Contact -->
<section class="slide col-2 row-3">
  <div class="band" style="width:260px;clip-path:polygon(0 0,260px 0,238px 41px,0 41px)"></div>
  <div class="badge" style="left:25px;top:14px">Ravenmoor<br>Detailing</div>
  <div class="photo" role="img" aria-label="Red mid-engine sports car, front three-quarter view" style="left:140px;top:15px;width:187px;height:160px;border-radius:50% 0 0 40%;background:radial-gradient(ellipse at 55% 55%,#d8262d 0%,#8e1519 45%,rgba(255,255,255,0) 72%)"></div>
  <div class="slide-title dark" style="top:45px">Contact <span class="accent">Us</span></div>
  <div class="body-copy" style="left:25px;top:67px;width:108px">Lorem ipsum dolor sit amet, consectetur adipiscing elit sed do eiusmod tempor incididunt ut labore et dolore magna aliqua. Ut enim ad minim veniam</div>
  <div class="contact-lines"><div>Address</div><div>Email</div><div>Website</div></div>
  <div class="dots"><span></span><span></span><span></span></div>
  <div class="footer-rule" style="right:150px"></div>
  <div class="page-no" style="left:23px;right:auto">08</div>
  <div class="footer-brand" style="left:41px">Vision to <span class="accent">Reality</span></div>
</section>

<!-- 9 Short break -->
<section class="slide dark-slide col-3 row-3">
  <div class="photo" role="img" aria-label="White brake caliper and drilled disc close-up" style="left:215px;top:0;width:112px;height:184px;background:linear-gradient(135deg,#6a6a6e,#1d1d1f)"></div>
  <div style="position:absolute;left:42px;top:16px;width:128px;height:110px;background:#0e0e0f"></div>
  <div class="brand-name" style="position:absolute;left:42px;top:60px;width:128px;font-size:12px;line-height:1.2">Ravenmoor<br>Detailing</div>
  <div class="slide-title" style="left:0;width:208px;text-align:center;top:130px;font-size:17px">Short <span class="accent">Break</span></div>
</section>

<!-- 10 Thank you -->
<section class="slide dark-slide col-1 row-4">
  <div style="position:absolute;left:218px;top:0;width:109px;height:184px;background:#242426"></div>
  <div class="brand-name" style="position:absolute;left:20px;top:70px;width:180px;font-size:20px;line-height:1.25">Ravenmoor<br>Detailing</div>
  <div class="slide-title" style="left:205px;top:83px;font-size:17px">THANK <span class="accent">YOU</span></div>
</section>

<div class="section-label" style="left:63px">Alternative Cover Slide</div>
<div class="section-label" style="left:428px">Alternative Content Slides</div>

<!-- Alt cover -->
<section class="slide dark-slide col-1 row-alt">
  <div class="photo" role="img" aria-label="Black sports coupe inside a warmly lit workshop" style="inset:0;background:radial-gradient(ellipse at 45% 60%,#8a6a3a 0%,#4d3a24 45%,#1c1a18 90%)"></div>
  <div style="position:absolute;left:0;right:0;bottom:0;height:20px;background:#141415"></div>
  <div style="position:absolute;left:40px;top:10px;width:240px;height:26px;background:#121213"></div>
  <div class="badge" style="left:40px;top:7px;width:56px;height:40px;font-size:5px">Ravenmoor Detailing</div>
  <div class="slide-title" style="left:105px;top:14px;font-size:22px;font-weight:700">Vision to Reality</div>
  <div class="names" style="bottom:7px"><span>Insert Name</span><span>Insert Name</span><span>Insert Name</span><span>Insert Name</span><span>Insert Name</span></div>
</section>

<!-- Alt content 1 -->
<section class="slide col-2 row-alt">
  <div class="band" style="width:260px;clip-path:polygon(0 0,260px 0,237px 41px,0 41px)"></div>
  <div class="slide-title" style="top:14px">GOALS &amp; <span class="accent">OBJECTIVES</span></div>
  <div class="badge" style="left:280px;top:14px">Ravenmoor<br>Detailing</div>
  <div class="goal-item" style="left:25px;top:61px;width:130px"><b>• Revenue Growth</b>Lorem ipsum dolor sit amet, consectetur adipiscing elit sed do eiusmod tempor.</div>
  <div class="goal-item" style="left:25px;top:84px;width:130px"><b>• Profit Margins</b>Lorem ipsum dolor sit amet, consectetur adipiscing elit sed do eiusmod tempor.</div>
  <div class="goal-item" style="left:25px;top:106px;width:130px"><b>• Sustainability</b>Lorem ipsum dolor sit amet, consectetur adipiscing elit sed do eiusmod tempor.</div>
  <div class="goal-item" style="left:25px;top:129px;width:130px"><b>• Return On Investment</b>Lorem ipsum dolor sit amet, consectetur adipiscing elit sed do eiusmod tempor.</div>
  <div class="goal-item" style="left:174px;top:61px;width:130px"><b>• Revenue Growth</b>Lorem ipsum dolor sit amet, consectetur adipiscing elit sed do eiusmod tempor.</div>
  <div class="goal-item" style="left:174px;top:84px;width:130px"><b>• Profit Margins</b>Lorem ipsum dolor sit amet, consectetur adipiscing elit sed do eiusmod tempor.</div>
  <div class="goal-item" style="left:174px;top:106px;width:130px"><b>• Sustainability</b>Lorem ipsum dolor sit amet, consectetur adipiscing elit sed do eiusmod tempor.</div>
  <div class="goal-item" style="left:174px;top:129px;width:130px"><b>• Return On Investment</b>Lorem ipsum dolor sit amet, consectetur adipiscing elit sed do eiusmod tempor.</div>
  <div class="footer-brand">Vision to <span class="accent">Reality</span></div>
  <div class="footer-rule"></div>
  <div class="page-no">03</div>
</section>

<!-- Alt content 2 -->
<section class="slide col-3 row-alt">
  <div class="photo" role="img" aria-label="White hatchback parked in a detailing bay, rear view" style="left:158px;top:0;width:169px;height:184px;background:linear-gradient(180deg,#3f4247,#8d9096 60%,#b8babd)"></div>
  <div class="band" style="width:260px;clip-path:polygon(0 0,260px 0,237px 41px,0 41px)"></div>
  <div class="slide-title" style="top:14px">GOALS &amp; <span class="accent">OBJECTIVES</span></div>
  <div class="badge" style="left:281px;top:14px">Ravenmoor<br>Detailing</div>
  <div class="goal-item" style="left:25px;top:67px;width:125px"><b>• Revenue Growth</b>Lorem ipsum dolor sit amet, consectetur adipiscing elit sed do eiusmod tempor.</div>
  <div class="goal-item" style="left:25px;top:89px;width:125px"><b>• Profit Margins</b>Lorem ipsum dolor sit amet, consectetur adipiscing elit sed do eiusmod tempor.</div>
  <div class="goal-item" style="left:25px;top:115px;width:125px"><b>• Sustainability</b>Lorem ipsum dolor sit amet, consectetur adipiscing elit sed do eiusmod tempor.</div>
  <div class="goal-item" style="left:25px;top:138px;width:125px"><b>• Return On Investment</b>Lorem ipsum dolor sit amet, consectetur adipiscing elit sed do eiusmod tempor.</div>
  <div class="footer-brand">Vision to <span class="accent">Reality</span></div>
  <div class="footer-rule" style="right:175px"></div>
  <div class="page-no" style="color:#ddd">03</div>
</section>

</div>
</body>
</html>
```